New business card for civil engineering company - "Keel Survey"

We need a business card designed for our new structural engineering company.

The company name is "Keel Survey" logo files attached.

We would like the following:
* Two-sided card
* Simple design

Information to be placed on the card:
Name - Marcus Hollby
Job Title - Director / Structural Engineer
Credentials - BEng(Hons), CPEng, CMengNZ, IntPE(NZ)
Email - marcus.hollby@keelsurvey-example.co.nz
mobile - 0219036458
website - www.keelsurvey-example.co.nz

```html
<!DOCTYPE html>
<html lang="en">
<head>
<meta charset="utf-8">
<title>Keel Survey – Business Card</title>
<link rel="stylesheet" href="https://fonts.googleapis.com/css2?family=Lato:wght@400;700&display=swap">
<style>
  :root {
    --backdrop: #e4e6e9;
    --card: #ffffff;
    --card-shade: #f1f2f4;
    --ink: #3a3d42;
    --ink-soft: #55595f;
    --accent: #2c7cc4;
    --accent-light: #8fc0e6;
  }
  * { box-sizing: border-box; margin: 0; padding: 0; }
  html, body {
    width: 1200px;
    height: 997px;
    overflow: hidden;
    background: var(--backdrop);
    font-family: "Lato", Arial, sans-serif;
    color: var(--ink);
  }
  .canvas { position: relative; width: 1200px; height: 997px; }
  .card {
    position: absolute;
    width: 620px;
    height: 354px;
    background: linear-gradient(135deg, var(--card) 0%, var(--card-shade) 100%);
    box-shadow: 0 6px 18px rgba(0,0,0,0.18);
  }
  .card-front { left: 70px; top: 90px; }
  .card-back { left: 510px; top: 530px; }

  .brand {
    display: flex;
    align-items: center;
    gap: 12px;
  }
  .brand-mark {
    width: 16px;
    height: 16px;
    background: var(--accent);
  }
  .brand-name {
    font-weight: 700;
    text-transform: uppercase;
    letter-spacing: 0.04em;
    color: var(--ink-soft);
  }
  .card-front .brand {
    position: absolute;
    left: 0; right: 0; top: 0; bottom: 0;
    justify-content: center;
  }
  .card-front .brand-name { font-size: 40px; }
  .card-front .brand-mark { width: 22px; height: 22px; }

  .card-back .brand {
    position: absolute;
    left: 42px;
    top: 56px;
  }
  .card-back .brand-name { font-size: 24px; }

  .holder {
    position: absolute;
    left: 42px;
    top: 128px;
  }
  .holder-name { font-size: 22px; font-weight: 700; color: var(--ink); }
  .holder-name .surname { font-weight: 400; }
  .holder-credentials { font-size: 13px; margin-top: 3px; color: var(--ink-soft); }
  .holder-role { font-size: 15px; margin-top: 3px; color: var(--accent); }

  .contact {
    position: absolute;
    left: 42px;
    top: 232px;
    list-style: none;
  }
  .contact li {
    display: flex;
    align-items: center;
    gap: 14px;
    font-size: 15px;
    color: var(--ink);
    margin-bottom: 9px;
  }
  .contact svg { width: 16px; height: 16px; fill: var(--accent); flex: none; }
</style>
</head>
<body>
<main class="canvas">

  <section class="card card-front" aria-label="Card front">
    <div class="brand">
      <span class="brand-mark"></span>
      <span class="brand-name">Keel Survey</span>
    </div>
  </section>

  <section class="card card-back" aria-label="Card back">
    <div class="brand">
      <span class="brand-mark"></span>
      <span class="brand-name">Keel Survey</span>
    </div>

    <div class="holder">
      <p class="holder-name">Marcus <span class="surname">Hollby</span></p>
      <p class="holder-credentials">BEng(Hons), CPEng, CMengNZ, IntPE(NZ)</p>
      <p class="holder-role">Director/ Structural Engineer</p>
    </div>

    <ul class="contact">
      <li>
        <svg viewBox="0 0 16 16" aria-hidden="true"><path d="M1 5c0-2 2-3 7-3s7 1 7 3v1.5h-4V5H5v1.5H1z M4 8h8l2 6H2z"/></svg>
        0219036458
      </li>
      <li>
        <svg viewBox="0 0 16 16" aria-hidden="true"><path d="M1 3h14v10H1z M2 4.2v.6l6 4 6-4v-.6z" fill-rule="evenodd"/></svg>
        marcus.hollby@keelsurvey-example.co.nz
      </li>
      <li>
        <svg viewBox="0 0 16 16" aria-hidden="true"><circle cx="8" cy="8" r="7"/><path d="M1 8h14M8 1v14M3 4h10M3 12h10" stroke="#fff" stroke-width="1" fill="none"/></svg>
        www.keelsurvey-example.co.nz
      </li>
    </ul>
  </section>

</main>
</body>
</html>
```